I would Like a design for our company's Elderflower Vodka. It is 70cl bottle, ( image of bottle attached) It will be 37.5% vol.The label would be nice to include a tasteful classy floral theme

```html
<!DOCTYPE html>
<html lang="en">
<head>
<meta charset="utf-8">
<title>Elderflower Vodka Label</title>
<link href="https://fonts.googleapis.com/css2?family=Lobster&family=Anton&family=Roboto:wght@400&display=swap" rel="stylesheet">
<style>
  :root {
    --page: #ffffff;
    --plum: #652d90;
    --orchid: #a764aa;
    --vine-light: rgba(255, 255, 255, 0.22);
    --vine-soft: rgba(255, 255, 255, 0.08);
    --ink: #2b2b2b;
    --white: #ffffff;
  }
  html, body {
    margin: 0;
    padding: 0;
    width: 1200px;
    height: 1200px;
    overflow: hidden;
    background: var(--page);
  }
  .canvas {
    width: 1200px;
    height: 1200px;
    position: relative;
  }
  .label-art {
    position: absolute;
    left: 0;
    top: 0;
    width: 1200px;
    height: 1200px;
  }
  .panel-dark { fill: var(--plum); }
  .panel-light { fill: var(--orchid); }
  .seal-ring { fill: var(--plum); }
  .seal-face { fill: var(--white); }
  .seal-name {
    font-family: "Roboto", Arial, sans-serif;
    font-weight: 400;
    font-size: 17px;
    letter-spacing: 2px;
    fill: var(--ink);
  }
  .flavour {
    font-family: "Lobster", cursive;
    font-size: 150px;
    fill: var(--white);
  }
  .spirit {
    font-family: "Anton", "Arial Narrow", sans-serif;
    font-size: 132px;
    letter-spacing: 2px;
    fill: var(--white);
  }
  .spec {
    font-family: "Roboto", Arial, sans-serif;
    font-size: 23px;
    fill: var(--white);
  }
</style>
</head>
<body>
<div class="canvas">
  <svg class="label-art" viewBox="0 0 1200 1200" xmlns="http://www.w3.org/2000/svg">
    <defs>
      <linearGradient id="vineFade" x1="0" y1="0" x2="0" y2="1">
        <stop offset="0" stop-color="#ffffff" stop-opacity="0.22"/>
        <stop offset="1" stop-color="#ffffff" stop-opacity="0.08"/>
      </linearGradient>
      <clipPath id="labelClip">
        <rect x="250" y="182" width="700" height="840"/>
      </clipPath>
    </defs>

    <g class="label" clip-path="url(#labelClip)">
      <rect class="panel-dark" x="250" y="182" width="700" height="840"/>
      <polygon class="panel-light" points="250,182 950,182 950,640"/>

      <g class="vine-decor" role="img" aria-label="Soft floral vine ornaments climbing both sides of the label">
        <rect x="255" y="190" width="170" height="832" rx="80" fill="url(#vineFade)"/>
        <rect x="770" y="200" width="180" height="822" rx="80" fill="url(#vineFade)"/>
        <rect x="380" y="190" width="360" height="150" rx="70" fill="var(--vine-soft)"/>
        <rect x="480" y="500" width="260" height="200" rx="90" fill="var(--vine-soft)"/>
      </g>
    </g>

    <g class="brand-seal">
      <circle class="seal-ring" cx="598" cy="432" r="116"/>
      <circle class="seal-face" cx="598" cy="432" r="108"/>
      <text class="seal-name" x="598" y="427" text-anchor="middle">LARKFIELD</text>
      <text class="seal-name" x="598" y="453" text-anchor="middle">DISTILLING CO.</text>
    </g>

    <text class="flavour" x="600" y="712" text-anchor="middle" transform="rotate(-9 600 672)">Elderflower</text>
    <text class="spirit" x="612" y="846" text-anchor="middle" transform="rotate(-9 612 788)">VODKA</text>

    <text class="spec" x="304" y="970">70 CL</text>
    <text class="spec" x="878" y="970" text-anchor="end">37.5% VOL</text>
  </svg>
</div>
</body>
</html>
```